Business Card for TVK, logo files already created

Please, can you assist with creating a Business card the TVK graphics which are already listed on www.brinmoretech.example
The business card should be modern and upmarket, textured designs are welcome. Please feel free to express yourself and be very bold with your design.

Target Market(s)

Cyber Security

Industry/Entity Type

Information Technology

Contact Information for Business Card

Company Name
Name
Title
Mobile
Fax or Tel
email
url

Font styles to use
Serif
Sans Serif

Colors
3277b5
85acd3
ffffff

```html
<!DOCTYPE html>
<html lang="en">
<head>
<meta charset="utf-8">
<title>TVK Business Card</title>
<link href="https://fonts.googleapis.com/css2?family=Montserrat:wght@300;400;700;800&family=Open+Sans:wght@400;600&display=swap" rel="stylesheet">
<style>
  :root {
    --navy: #121a48;
    --navy-deep: #0f1640;
    --teal: #1e6d82;
    --brand-blue: #3277b5;
    --brand-light: #85acd3;
    --paper: #f6f5f1;
    --ink: #1b2560;
    --grey: #8a8d98;
    --rule: #b9bcc6;
    --stage: #e4e5e9;
    --white: #ffffff;
  }
  * { margin: 0; padding: 0; box-sizing: border-box; }
  html, body { width: 1200px; height: 900px; overflow: hidden; }
  body {
    background: var(--stage);
    font-family: "Open Sans", sans-serif;
    display: flex;
    flex-direction: column;
    align-items: center;
    justify-content: center;
    gap: 40px;
  }
  .card {
    position: relative;
    width: 630px;
    height: 360px;
    overflow: hidden;
    box-shadow: 0 10px 28px rgba(0,0,0,.18);
  }

  /* Front */
  .card-front {
    background: linear-gradient(180deg, var(--navy-deep) 0%, var(--navy) 55%, var(--teal) 100%);
  }
  .card-front .arcs { position: absolute; inset: 0; }
  .front-brand {
    position: absolute;
    left: 50%; top: 50%;
    transform: translate(-50%, -55%);
    display: flex; align-items: center; gap: 18px;
  }
  .brand-dot {
    width: 44px; height: 44px; border-radius: 50%;
    background: var(--brand-light);
  }
  .brand-name {
    font-family: "Montserrat", sans-serif;
    font-weight: 800;
    font-size: 96px;
    letter-spacing: 4px;
    line-height: 1;
    color: var(--brand-light);
  }

  /* Back */
  .card-back {
    background: var(--paper);
    background-image: radial-gradient(rgba(0,0,0,.025) 1px, transparent 1px);
    background-size: 4px 4px;
  }
  .back-brand {
    position: absolute;
    right: 44px; top: 34px;
    display: flex; align-items: center; gap: 10px;
  }
  .back-brand .brand-dot { width: 22px; height: 22px; background: var(--brand-blue); }
  .back-brand .brand-name { font-size: 52px; letter-spacing: 2px; color: var(--brand-blue); }

  .divider-h {
    position: absolute;
    left: 40px; right: 40px; top: 198px;
    height: 1px; background: var(--rule);
  }
  .divider-v {
    position: absolute;
    left: 345px; top: 222px;
    width: 1px; height: 40px; background: var(--ink);
  }
  .person {
    position: absolute; left: 44px; top: 160px;
    font-family: "Montserrat", sans-serif;
  }
  .person-name { font-size: 21px; color: var(--ink); letter-spacing: .5px; }
  .person-name strong { font-weight: 800; }
  .person-name span { font-weight: 300; }
  .person-title {
    font-size: 11px; color: var(--grey); letter-spacing: 1px;
    margin-top: 18px;
  }
  .contact-list { list-style: none; position: absolute; font-size: 15px; color: var(--ink); }
  .contact-list li { display: flex; align-items: center; gap: 10px; margin-bottom: 8px; }
  .contact-list svg { width: 14px; height: 14px; fill: var(--ink); flex: none; }
  .contact-phones { left: 44px; top: 258px; }
  .contact-web { left: 380px; top: 218px; font-size: 14px; }
</style>
</head>
<body>

<section class="card card-front" aria-label="Card front">
  <svg class="arcs" viewBox="0 0 630 360" aria-hidden="true">
    <circle cx="640" cy="110" r="110" fill="none" stroke="#3f6fa8" stroke-opacity=".45" stroke-width="1"/>
    <circle cx="660" cy="140" r="70" fill="none" stroke="#3f6fa8" stroke-opacity=".35" stroke-width="1"/>
    <circle cx="-40" cy="180" r="120" fill="none" stroke="#3f6fa8" stroke-opacity=".25" stroke-width="1"/>
  </svg>
  <div class="front-brand">
    <div class="brand-dot"></div>
    <div class="brand-name">TVK</div>
  </div>
</section>

<section class="card card-back" aria-label="Card back">
  <div class="back-brand">
    <div class="brand-dot"></div>
    <div class="brand-name">TVK</div>
  </div>

  <div class="person">
    <div class="person-name"><strong>ROWAN</strong> <span>ELLERY</span></div>
    <div class="person-title">FOUNDER AND CEO</div>
  </div>

  <div class="divider-h"></div>
  <div class="divider-v"></div>

  <ul class="contact-list contact-phones">
    <li>
      <svg viewBox="0 0 16 16"><path d="M4 0h8a1 1 0 0 1 1 1v14a1 1 0 0 1-1 1H4a1 1 0 0 1-1-1V1a1 1 0 0 1 1-1zm0 2v11h8V2zm3 12v1h2v-1z"/></svg>
      123-456-7890
    </li>
    <li>
      <svg viewBox="0 0 16 16"><path d="M1 6c0-3 3-4 7-4s7 1 7 4l-3 1-1-2H5L4 7zM3 9l2-2h6l2 2v5H3zm5 1.5a1.5 1.5 0 1 0 0 3 1.5 1.5 0 0 0 0-3z"/></svg>
      123-456-7890
    </li>
  </ul>

  <ul class="contact-list contact-web">
    <li>
      <svg viewBox="0 0 16 16"><path d="M1 3h14v10H1zm1.5 1.2V12h11V4.2L8 8.5z M2.8 4 8 7.8 13.2 4z"/></svg>
      contact@brinmoretech.example
    </li>
    <li>
      <svg viewBox="0 0 16 16"><path d="M8 0a8 8 0 1 0 0 16A8 8 0 0 0 8 0zm5.9 7h-2.5a12 12 0 0 0-1-4.6A6 6 0 0 1 13.9 7zM8 2c.8 1.1 1.3 3 1.4 5H6.6C6.7 5 7.2 3.1 8 2zM5.6 2.4A12 12 0 0 0 4.6 7H2.1a6 6 0 0 1 3.5-4.6zM2.1 9h2.5a12 12 0 0 0 1 4.6A6 6 0 0 1 2.1 9zM8 14c-.8-1.1-1.3-3-1.4-5h2.8c-.1 2-.6 3.9-1.4 5zm2.4-.4a12 12 0 0 0 1-4.6h2.5a6 6 0 0 1-3.5 4.6z"/></svg>
      www.brinmoretech.example
    </li>
  </ul>
</section>

</body>
</html>
```